Buch-/eBook-Cover für psychologische Beratung
Mirell hat sehr gut verstanden worauf es mir ankam und hat das Cover sehr gut auf das bereits bestehende abgestimmt. Sie hat zuverlässig geantwortet und Korrekturwünsche präzise ausgeführt. Grosses Kompliment! Gerne wieder.
Zielgruppe
psychologische Beratung, Zielgruppe Frauen
Aufgabenstellung
Es ist ein bestehendes ebook, das ich über meine frühere Website gekauft habe. Diese wird aufgelöst. Das ebook ist nun auf brixa und soll auch auf kolvento, aber offensichtlich zieht der Titel nicht. Deshalb möchte ich den ändern.
Der neue Titel und Untertitel lautet: Atmen statt zweifeln. Leises Naschen deuten, alte Muster entwirren.
Meine Idee wäre es, als Blickfang das Wort 'Atmen' und 'Leises Naschen' hervorzuheben.
Es ist mir wichtig, dass - vielleicht mit einer Andeutung eines Tellers - sofort klar wird, dass es um Essen geht.
Das Design soll passend zum Inhalt sein (Schrift und Illustrationen).
Das eBook ist im Querformat gehalten, weil es ein Arbeitsbuch ist. Für die Werbung brauche ich aber zusätzlich eine Version, die ins Hochformat passt.
Das Design darf nicht zu überladen sein.

```html
<!DOCTYPE html>
<html lang="de">
<head>
<meta charset="utf-8">
<title>Atmen statt zweifeln – Cover</title>
<link rel="stylesheet" href="https://fonts.googleapis.com/css2?family=Allura&family=Outfit:wght@300;400;600&display=swap">
<style>
  :root {
    --backdrop: #e6e6ea;
    --paper: #ffffff;
    --cream: #fff0d2;
    --orange: #f09a55;
    --ink: #2e2e2e;
  }
  * { margin: 0; padding: 0; box-sizing: border-box; }
  html, body {
    width: 1200px; height: 1200px; overflow: hidden;
    background: var(--backdrop);
  }
  .cover {
    position: absolute;
    left: 147px; top: 275px;
    width: 865px; height: 610px;
    background: var(--paper);
    overflow: hidden;
    font-family: "Outfit", sans-serif;
    color: var(--ink);
  }
  .cover__shapes { position: absolute; inset: 0; width: 100%; height: 100%; }
  .cover__title-script {
    position: absolute; left: 58px; top: 70px;
    font-family: "Allura", cursive;
    font-size: 150px; line-height: 1;
    color: var(--orange);
    font-weight: 400;
  }
  .cover__title-rest {
    position: absolute; left: 64px; top: 202px;
    font-size: 31px; font-weight: 300; letter-spacing: 0.2px;
  }
  .cover__subtitle-accent {
    position: absolute; left: 64px; top: 316px;
    font-size: 30px; font-weight: 600; line-height: 1.3;
    color: var(--orange);
  }
  .cover__subtitle-rest {
    position: absolute; left: 64px; top: 425px;
    font-size: 23px; font-weight: 300; line-height: 1.4;
  }
  .cover__author {
    position: absolute; left: 64px; top: 522px;
    font-size: 18px; font-weight: 300;
  }
</style>
</head>
<body>
  <main class="cover">
    <svg class="cover__shapes" viewBox="0 0 865 610" preserveAspectRatio="none">
      <defs>
        <linearGradient id="table-setting-tone" x1="0" y1="0" x2="1" y2="1">
          <stop offset="0" stop-color="#fff0d2" stop-opacity="0.6"/>
          <stop offset="1" stop-color="#e88a44" stop-opacity="0.6"/>
        </linearGradient>
      </defs>
      <path class="shape-cream" fill="var(--cream)"
        d="M453 0 C400 40 390 110 402 160 C415 220 420 280 400 360 C370 470 330 560 288 610 L865 610 L865 0 Z"/>
      <path class="shape-orange" fill="var(--orange)"
        d="M288 610 C400 560 460 490 513 415 C580 330 640 280 693 247 C770 195 820 160 865 136 L865 610 Z"/>
      <rect class="table-setting" x="420" y="232" width="432" height="292" rx="6"
        fill="url(#table-setting-tone)" role="img"
        aria-label="Einzeilige Strichzeichnung: Gabel, Teller mit Herz und Messer, verbunden durch eine Linie"/>
    </svg>

    <h1 class="cover__title">
      <span class="cover__title-script">Atmen</span>
      <span class="cover__title-rest">statt zweifeln.</span>
    </h1>
    <p class="cover__subtitle-accent">Leises<br>Naschen</p>
    <p class="cover__subtitle-rest">deuten, alte<br>Muster entwirren.</p>
    <p class="cover__author">Lene Varholm</p>
  </main>
</body>
</html>
```